Aisle signage for supermarket

Design Isle signs for Indian supermarket. Modern, Clear, legible. Would be nice to use our logo colours. Signs Will be double sided and measure 900mm width x 400mm height. Indian theme would be nice. Attached files shows description to go on each sign.
Font styles to use
Sans Serif
Colors
Designer to choose colors to be used in the design.

```html
<!DOCTYPE html>
<html lang="en">
<head>
<meta charset="utf-8">
<title>Aisle Signs</title>
<link href="https://fonts.googleapis.com/css2?family=Montserrat:wght@700;800;900&display=swap" rel="stylesheet">
<style>
  :root {
    --backdrop: #3a3a3a;
    --leaf: #8dc63f;
    --leaf-band: #b3db78;
    --leaf-motif: #82bb39;
    --forest: #006837;
    --white: #ffffff;
  }
  html, body {
    margin: 0;
    padding: 0;
    width: 1125px;
    height: 1200px;
    overflow: hidden;
    background: var(--backdrop);
  }
  .canvas {
    position: relative;
    width: 1125px;
    height: 1200px;
  }
  .aisle-sign {
    position: absolute;
    left: 71px;
    width: 983px;
    height: 436px;
    background: var(--leaf);
    overflow: hidden;
  }
  .aisle-sign--one { top: 94px; }
  .aisle-sign--three { top: 670px; }

  .border-band {
    position: absolute;
    inset: 0;
    border: 21px solid var(--leaf-band);
    box-sizing: border-box;
  }
  .border-band::after {
    content: "";
    position: absolute;
    inset: 2px;
    border: 1.5px solid var(--white);
  }
  .motif {
    position: absolute;
    left: 101px;
    top: 168px;
    width: 492px;
    height: 233px;
    background: radial-gradient(ellipse at 50% 30%, var(--leaf-motif) 0%, var(--leaf-motif) 45%, rgba(130,187,57,0) 72%);
  }
  .category {
    position: absolute;
    left: 45px;
    width: 604px;
    height: 121px;
    background: var(--white);
    display: flex;
    align-items: center;
    box-sizing: border-box;
    padding-left: 69px;
    font-family: "Montserrat", sans-serif;
    font-weight: 800;
    font-size: 46px;
    letter-spacing: -0.5px;
    color: var(--forest);
  }
  .category--upper { top: 47px; }
  .category--lower { top: 189px; height: 120px; }

  .aisle-number {
    position: absolute;
    left: 666px;
    top: 47px;
    width: 271px;
    height: 262px;
    background: var(--forest);
    display: flex;
    align-items: center;
    justify-content: center;
    font-family: "Montserrat", sans-serif;
    font-weight: 900;
    font-size: 236px;
    line-height: 1;
    color: var(--white);
  }
  .aisle-number::before {
    content: "";
    position: absolute;
    inset: 9px;
    border: 1.5px solid var(--leaf);
  }
  .store-name {
    position: absolute;
    left: 673px;
    top: 338px;
    width: 257px;
    text-align: center;
    font-family: "Montserrat", sans-serif;
    font-weight: 700;
    font-size: 32px;
    letter-spacing: 1px;
    color: var(--white);
  }
</style>
</head>
<body>
<main class="canvas">
  <section class="aisle-sign aisle-sign--one">
    <div class="border-band" role="img" aria-label="Indian geometric pattern border"></div>
    <div class="motif" role="img" aria-label="Faint mandala ornament"></div>
    <div class="category category--upper">JUICES</div>
    <div class="category category--lower">SOFT DRINKS</div>
    <div class="aisle-number">1</div>
    <div class="store-name">KESAR MART</div>
  </section>

  <section class="aisle-sign aisle-sign--three">
    <div class="border-band" role="img" aria-label="Indian geometric pattern border"></div>
    <div class="motif" role="img" aria-label="Faint mandala ornament"></div>
    <div class="category category--upper">OILS / GHEE</div>
    <div class="category category--lower">CANNED PRODUCTS</div>
    <div class="aisle-number">3</div>
    <div class="store-name">KESAR MART</div>
  </section>
</main>
</body>
</html>
```